BHSC Business cards

We are an established dental practice that is looking for new business cards to match our new logo. We are looking for something unique and sophisticated.
BRIEF: Colours are black, silver and white. Include the company name, logo (including “Pelwick Heath Dental Care”) and phone number “03 9415 2876”.
Front - Include the company name, logo (including “Pelwick Heath Dental Care”) and phone number “03 9415 2876”.
Back - Include the company name,  “Pelwick Heath Dental Care”, phone number “03 9415 2876”. address "64A Tindle Street, Pelwick Heath, Vic 3187", "Email reception@pelwickheathdentalcare.com.au", the Dentist Name " Dr ................................"  Your next appointment "Day, date and time(am/pm)".  3 lines for 3 appointments please, and at the bottom "IF UNABLE TO KEEP THIS APPOINTMENT 48 HOURS NOTICE IS REQUIRED."
Try and be creative and different with the design, i've added an image for inspiration

Target Market(s)
ALL in need of dental
Industry/Entity Type
Dental Clinic
Look and feel
Each slider illustrates characteristics of the customer's brand and the style your logo design should communicate.

```html
<!DOCTYPE html>
<html lang="en">
<head>
<meta charset="utf-8">
<title>Pelwick Heath Dental Care – Business Cards</title>
<link href="https://fonts.googleapis.com/css2?family=Lato:wght@400;700;900&display=swap" rel="stylesheet">
<style>
  :root {
    --backdrop: #566a91;
    --card-dark: #1f1f23;
    --card-light: #ffffff;
    --ink: #141416;
    --silver: #c9c9cc;
    --silver-soft: #e4e4e6;
    --shadow: 0 2px 5px rgba(0,0,0,0.25);
  }
  * { margin: 0; padding: 0; box-sizing: border-box; }
  html, body {
    width: 1200px; height: 1200px; overflow: hidden;
    background: var(--backdrop);
    font-family: "Lato", Arial, sans-serif;
  }
  .sheet { position: relative; width: 1200px; height: 1200px; }
  .card {
    position: absolute; width: 484px; height: 276px;
    box-shadow: var(--shadow); overflow: hidden;
  }
  .card--dark { background: var(--card-dark); color: #fff; }
  .card--light { background: var(--card-light); color: var(--ink); }
  .front-dark { left: 88px; top: 303px; }
  .front-light { left: 629px; top: 303px; }
  .back-light { left: 88px; top: 620px; }
  .back-dark { left: 629px; top: 620px; }

  /* Brand lockup: plain circle + name */
  .brand { position: absolute; text-align: center; font-weight: 700; }
  .brand__mark { display: block; margin: 0 auto; border-radius: 50%; }
  .brand__name { display: block; text-transform: uppercase; white-space: nowrap; }
  .brand__sub { display: block; text-transform: uppercase; white-space: nowrap; }

  .card--dark .brand { color: var(--silver); }
  .card--dark .brand__mark { background: var(--silver); }
  .card--light .brand { color: var(--ink); }
  .card--light .brand__mark { background: var(--ink); }

  .front .brand { left: 0; right: 0; top: 43px; }
  .front .brand__mark { width: 100px; height: 100px; }
  .front .brand__name { margin-top: 14px; font-size: 31px; letter-spacing: 1px; line-height: 1; }
  .front .brand__sub { margin-top: 6px; font-size: 15px; letter-spacing: 4px; line-height: 1; }
  .front__phone {
    position: absolute; left: 0; right: 0; top: 217px; text-align: center;
    font-size: 21px; letter-spacing: 2.5px; font-weight: 400;
  }
  .card--dark .front__phone { color: var(--silver-soft); }

  .back .brand__mark { width: 50px; height: 50px; }
  .back .brand__name { margin-top: 4px; font-size: 16px; line-height: 1; }
  .back .brand__sub { margin-top: 2px; font-size: 8px; letter-spacing: 2px; line-height: 1; }
  .back-light .brand { left: 306px; width: 160px; top: 9px; }
  .back-dark .brand { left: 302px; width: 160px; top: 81px; }
  .card--dark.back .brand { color: #fff; }
  .card--dark.back .brand__mark { background: #fff; }

  .contact { position: absolute; }
  .contact__title { font-size: 20px; font-weight: 700; letter-spacing: 0.3px; line-height: 1; }
  .contact__line { font-size: 9px; font-weight: 700; letter-spacing: 0.8px; line-height: 1; }
  .back-light .contact { left: 23px; top: 19px; }
  .back-light .contact__phone { margin-top: 7px; }
  .back-light .contact__address { margin-top: 7px; }
  .back-light .contact__email { margin-top: 7px; letter-spacing: 0.3px; }
  .back-dark .contact { left: 0; right: 0; top: 17px; text-align: center; }
  .back-dark .contact__phone { margin-top: 4px; }
  .back-dark .contact__address { margin-top: 11px; }
  .back-dark .contact__email { margin-top: 9px; letter-spacing: 0.3px; }

  .appointment__title { position: absolute; font-size: 19px; letter-spacing: 1px; font-weight: 400; line-height: 1; }
  .back-light .appointment__title { left: 0; right: 0; top: 133px; text-align: center; }
  .back-dark .appointment__title { left: 24px; top: 125px; }

  .slots { position: absolute; left: 23px; right: 23px; top: 171px; list-style: none; }
  .slot { display: flex; align-items: baseline; height: 21px; font-size: 12px; letter-spacing: 1.5px; }
  .slot__label { white-space: nowrap; }
  .slot__fill { border-bottom: 1px dotted currentColor; margin: 0 2px; height: 1px; align-self: center; position: relative; top: 3px; }
  .slot__fill--date { width: 214px; }
  .slot__fill--time { flex: 1; }
  .slot__meridiem { font-size: 9px; letter-spacing: 0.3px; }

  .notice {
    position: absolute; left: 0; right: 0; top: 249px; text-align: center;
    font-size: 10px; letter-spacing: 0; font-weight: 400;
  }
</style>
</head>
<body>
<main class="sheet">

  <section class="card card--dark front front-dark">
    <div class="brand">
      <span class="brand__mark"></span>
      <span class="brand__name">Pelwick Heath</span>
      <span class="brand__sub">— Dental Care —</span>
    </div>
    <p class="front__phone">03 9415 2876</p>
  </section>

  <section class="card card--light front front-light">
    <div class="brand">
      <span class="brand__mark"></span>
      <span class="brand__name">Pelwick Heath</span>
      <span class="brand__sub">— Dental Care —</span>
    </div>
    <p class="front__phone">03 9415 2876</p>
  </section>

  <section class="card card--light back back-light">
    <div class="contact">
      <p class="contact__title">TELEPHONE</p>
      <p class="contact__line contact__phone">03 9415 2876</p>
      <p class="contact__line contact__address">64A Tindle Street, Pelwick Heath Vic 3187</p>
      <p class="contact__line contact__email">reception@pelwickheathdentalcare.com.au</p>
    </div>
    <div class="brand">
      <span class="brand__mark"></span>
      <span class="brand__name">Pelwick Heath</span>
      <span class="brand__sub">— Dental Care —</span>
    </div>
    <h2 class="appointment__title">Appointment</h2>
    <ul class="slots">
      <li class="slot"><span class="slot__label">Date :</span><span class="slot__fill slot__fill--date"></span><span class="slot__label">Time :</span><span class="slot__fill slot__fill--time"></span><span class="slot__meridiem">AM/PM</span></li>
      <li class="slot"><span class="slot__label">Date :</span><span class="slot__fill slot__fill--date"></span><span class="slot__label">Time :</span><span class="slot__fill slot__fill--time"></span><span class="slot__meridiem">AM/PM</span></li>
      <li class="slot"><span class="slot__label">Date :</span><span class="slot__fill slot__fill--date"></span><span class="slot__label">Time :</span><span class="slot__fill slot__fill--time"></span><span class="slot__meridiem">AM/PM</span></li>
    </ul>
    <p class="notice">IF UNABLE TO KEEP THIS APPOINTMENT 48 HOURS NOTICE IS REQUIRED</p>
  </section>

  <section class="card card--dark back back-dark">
    <div class="contact">
      <p class="contact__title">TELEPHONE</p>
      <p class="contact__line contact__phone">03 9415 2876</p>
      <p class="contact__line contact__address">64A Tindle Street, Pelwick Heath Vic 3187</p>
      <p class="contact__line contact__email">reception@pelwickheathdentalcare.com.au</p>
    </div>
    <h2 class="appointment__title">Appointment</h2>
    <div class="brand">
      <span class="brand__mark"></span>
      <span class="brand__name">Pelwick Heath</span>
      <span class="brand__sub">— Dental Care —</span>
    </div>
    <ul class="slots">
      <li class="slot"><span class="slot__label">Date :</span><span class="slot__fill slot__fill--date"></span><span class="slot__label">Time :</span><span class="slot__fill slot__fill--time"></span><span class="slot__meridiem">AM/PM</span></li>
      <li class="slot"><span class="slot__label">Date :</span><span class="slot__fill slot__fill--date"></span><span class="slot__label">Time :</span><span class="slot__fill slot__fill--time"></span><span class="slot__meridiem">AM/PM</span></li>
      <li class="slot"><span class="slot__label">Date :</span><span class="slot__fill slot__fill--date"></span><span class="slot__label">Time :</span><span class="slot__fill slot__fill--time"></span><span class="slot__meridiem">AM/PM</span></li>
    </ul>
    <p class="notice">IF UNABLE TO KEEP THIS APPOINTMENT 48 HOURS NOTICE IS REQUIRED</p>
  </section>

</main>
</body>
</html>
```